Halloway Crest Backers Guild business cards

Create a single-sided business card for the Halloway Crest Backers Guild based on the attached logo.
The additional data fields include Name, Title, Email, Phone, and website.
Please use the following as sample data:
Name: Dean Varrow
Title: Co-Founder / Investor
Email: deanvarrow@mailtern.net
Phone: 555-314-2706
Website: www.hcbackersguild.com

Target Market(s)

Start ups, entrepreneurs, venture capitalists

Industry/Entity Type

Investment

Contact Information for Business Card

Professional business card. Technology company.

Font styles to use
Serif
Sans Serif

Requirements
Must have
• Include the HCBG logo (attached)
• Name
• Title
• Email
• Phone
• Website
Should not have
• Cute, cartoony

```html
<!DOCTYPE html>
<html lang="en">
<head>
<meta charset="UTF-8">
<title>Halloway Crest Backers Guild – Business Card</title>
<link rel="stylesheet" href="https://fonts.googleapis.com/css2?family=Open+Sans:wght@400;600;700&family=Arimo:wght@400;700&display=swap">
<style>
  :root {
    --backdrop: #2b2b2b;
    --card-white: #f4f4f4;
    --card-black: #050505;
    --brand-green: #129a4f;
    --ink-dark: #2a2a2a;
    --ink-light: #e6e6e6;
  }
  * { margin: 0; padding: 0; box-sizing: border-box; }
  html, body {
    width: 1200px;
    height: 997px;
    overflow: hidden;
    background: var(--backdrop);
  }
  .canvas {
    position: relative;
    width: 1200px;
    height: 997px;
  }
  .card {
    position: absolute;
    left: 150px;
    top: 241px;
    width: 900px;
    height: 514px;
    background: var(--card-black);
    overflow: hidden;
    box-shadow: 0 20px 50px rgba(0,0,0,0.55);
  }
  .card-top {
    position: absolute;
    inset: 0 0 auto 0;
    height: 272px;
    background: linear-gradient(180deg, #ffffff 0%, var(--card-white) 100%);
  }
  .accent-rule {
    position: absolute;
    left: 0;
    right: 0;
    top: 272px;
    height: 7px;
    background: var(--brand-green);
  }
  .accent-notch {
    position: absolute;
    left: 52px;
    top: 278px;
    width: 0;
    height: 0;
    border-left: 12px solid transparent;
    border-right: 12px solid transparent;
    border-top: 12px solid var(--brand-green);
  }
  .brand {
    position: absolute;
    top: 108px;
    left: 0;
    right: 0;
    display: flex;
    align-items: center;
    justify-content: center;
    gap: 22px;
  }
  .brand-square {
    width: 46px;
    height: 46px;
    background: var(--brand-green);
  }
  .brand-name {
    font-family: "Open Sans", sans-serif;
    font-weight: 700;
    font-size: 34px;
    letter-spacing: 0.5px;
    color: var(--ink-dark);
    text-transform: uppercase;
  }
  .holder {
    position: absolute;
    left: 62px;
    top: 300px;
    font-family: "Arimo", sans-serif;
  }
  .holder-name {
    font-size: 30px;
    color: var(--brand-green);
    text-transform: uppercase;
    letter-spacing: 0.5px;
    line-height: 1.1;
  }
  .holder-title {
    font-size: 18px;
    color: var(--ink-light);
    margin-top: 4px;
  }
  .contact-list {
    position: absolute;
    left: 62px;
    top: 412px;
    list-style: none;
    font-family: "Arimo", sans-serif;
    font-size: 24px;
    color: var(--ink-light);
  }
  .contact-item {
    display: flex;
    align-items: center;
    gap: 14px;
    margin-bottom: 10px;
  }
  .contact-icon {
    width: 24px;
    height: 24px;
    flex: none;
  }
  .website {
    position: absolute;
    right: 56px;
    top: 320px;
    font-family: "Arimo", sans-serif;
    font-weight: 700;
    font-size: 21px;
    letter-spacing: 2px;
    color: var(--brand-green);
  }
</style>
</head>
<body>
<main class="canvas">
  <section class="card" aria-label="Business card for Dean Varrow">
    <div class="card-top">
      <div class="brand">
        <span class="brand-square" aria-hidden="true"></span>
        <span class="brand-name">Halloway Crest Backers Guild</span>
      </div>
    </div>
    <div class="accent-rule"></div>
    <div class="accent-notch"></div>

    <div class="holder">
      <p class="holder-name">Dean Varrow</p>
      <p class="holder-title">Co-Founder / Investor</p>
    </div>

    <p class="website">www.hcbackersguild.com</p>

    <ul class="contact-list">
      <li class="contact-item">
        <svg class="contact-icon" viewBox="0 0 24 24" aria-hidden="true">
          <circle cx="12" cy="12" r="12" fill="#129a4f"/>
          <path d="M8.5 6.5l2 2-1.2 1.6c.8 1.7 2 2.9 3.6 3.6l1.6-1.2 2 2-1.2 1.8c-3.9-.6-7.6-4.3-8.2-8.2z" fill="#050505"/>
        </svg>
        <span>555-314-2706</span>
      </li>
      <li class="contact-item">
        <svg class="contact-icon" viewBox="0 0 24 24" aria-hidden="true">
          <circle cx="12" cy="12" r="12" fill="#129a4f"/>
          <rect x="6" y="8" width="12" height="8.5" fill="#050505"/>
          <path d="M6 8l6 5 6-5" fill="none" stroke="#129a4f" stroke-width="1.2"/>
        </svg>
        <span>deanvarrow@mailtern.net</span>
      </li>
    </ul>
  </section>
</main>
</body>
</html>
```